Upmarket cover for top management book, ideally unlike most common cover pages

This book is about both good management and mismanagement and introduces novel concepts such as the inverse exponential law in strategy, No doubt that these concepts will be criticized by some management scholars. However, students, a few other colleagues and key top managers find the new ideas useful and eye-opening.
The cover must help communicate a deeper vision of management as an expression of life creation and a sort of "divine" energy.

Practical details:
Print and ebook cover page plus elements of the cover for each of the three main book sections.
Title; The Harbor
Subtitle: Field methods and the quiet ripple rule
Author: Teodor M. Vasquel
Publisher: Brightwell Page Press
Width x height: 13,97 x 21,59 cm (without bleed)
Spine: 14-15 cm according to paper color

Target Market(s)

Mostly managers who did not have the opportunity of attending postgraduate management studies such as the MBA

Industry/Entity Type

Mostly high technology

Font styles to use
Serif
Sans Serif
Other font styles liked:
• Arial nova, Arial light

Requirements
Must have
• Preferably cover and back cover on white background, but any good proposals would do.
Nice to have
• An image of bright and reassuring, albeit potentially unlimited, strength. Ideally the cover design should show that good management is good for the COMMON GOOD of society
Should not have
• Please do not show images of people and no proposals reminiscent of other management and strategy book covers

```html
<!DOCTYPE html>
<html lang="en">
<head>
<meta charset="utf-8">
<title>The Harbor — Teodor M. Vasquel</title>
<link rel="stylesheet" href="https://fonts.googleapis.com/css2?family=Barlow:wght@400;700&family=Playfair+Display:wght@400&display=swap">
<style>
  :root {
    --cover-red: #ff0000;
    --cover-grey: #8f8f8f;
    --ink-white: #ffffff;
    --figure-tone: rgba(255, 255, 255, 0.88);
    --serif: "Playfair Display", "Bodoni 72", serif;
    --sans: "Barlow", "Arial", sans-serif;
  }
  html, body {
    margin: 0;
    padding: 0;
    width: 1200px;
    height: 885px;
    overflow: hidden;
    background: var(--cover-red);
  }
  .cover {
    position: relative;
    width: 1200px;
    height: 885px;
    overflow: hidden;
    background: var(--cover-red);
    color: var(--ink-white);
  }
  .cover-art {
    position: absolute;
    inset: 0;
    width: 1200px;
    height: 885px;
  }
  .back-quote {
    position: absolute;
    right: 701px;
    top: 105px;
    margin: 0;
    font-family: var(--sans);
    font-size: 19px;
    line-height: 20.2px;
    text-align: right;
    white-space: nowrap;
  }
  .back-attribution {
    position: absolute;
    left: 64px;
    top: 534px;
    margin: 0;
    font-family: var(--sans);
    font-size: 16.5px;
    line-height: 20px;
  }
  .back-attribution strong {
    font-weight: 700;
    font-size: 18px;
  }
  .front-subtitle {
    position: absolute;
    left: 940px;
    top: 106px;
    margin: 0;
    font-family: var(--sans);
    font-size: 22px;
    line-height: 21.5px;
    font-weight: 400;
  }
  .front-author {
    position: absolute;
    left: 1014px;
    top: 742px;
    margin: 0;
    font-family: var(--sans);
    font-size: 46px;
    line-height: 42px;
    font-weight: 400;
    letter-spacing: -0.5px;
  }
  .title-serif { font-family: var(--serif); fill: var(--ink-white); }
  .spine-sans { font-family: var(--sans); fill: var(--ink-white); }
</style>
</head>
<body>
<main class="cover">
  <svg class="cover-art" viewBox="0 0 1200 885" xmlns="http://www.w3.org/2000/svg">
    <!-- front panel grey field with sweeping curve -->
    <path class="front-field" fill="var(--cover-grey)"
          d="M918 0 H1200 V885 H985 C978 800 945 735 883 676 L918 640 Z"/>

    <!-- spine -->
    <g class="spine">
      <text class="spine-sans" transform="translate(605 239) rotate(-90)" font-size="18" textLength="203" lengthAdjust="spacingAndGlyphs">Brightwell Page Press</text>
      <text class="spine-sans" transform="translate(612 601) rotate(-90)" font-size="34" textLength="205" lengthAdjust="spacingAndGlyphs">TEODOR M. VASQUEL</text>
      <rect class="spine-divider" x="589" y="620" width="28" height="3" fill="var(--ink-white)"/>
      <text class="title-serif" transform="translate(610 851) rotate(-90)" font-size="38" textLength="208" lengthAdjust="spacingAndGlyphs">The Harbor</text>
    </g>

    <!-- front title -->
    <g class="front-title">
      <text class="title-serif" transform="translate(724 203) rotate(-90)" font-size="80" textLength="117" lengthAdjust="spacingAndGlyphs">The</text>
      <text class="title-serif" x="707" y="205" font-size="300" textLength="211" lengthAdjust="spacingAndGlyphs">H</text>
      <text class="title-serif" x="897" y="337" font-size="245" textLength="254" lengthAdjust="spacingAndGlyphs">ar</text>
      <text class="title-serif" x="902" y="469" font-size="245" textLength="244" lengthAdjust="spacingAndGlyphs">bo</text>
      <text class="title-serif" x="838" y="672" font-size="245" textLength="150" lengthAdjust="spacingAndGlyphs">r</text>
    </g>

    <!-- walking figure placeholders -->
    <g class="walker" role="img" aria-label="Small white silhouette of a walking person casting a shadow">
      <rect x="764" y="363" width="19" height="65" rx="8" fill="var(--figure-tone)"/>
    </g>
    <g class="walker" role="img" aria-label="Small white silhouette of a walking person casting a shadow">
      <rect x="815" y="428" width="20" height="61" rx="8" fill="var(--figure-tone)"/>
    </g>
    <g class="walker" role="img" aria-label="Small white silhouette of a walking person casting a shadow">
      <rect x="716" y="699" width="22" height="64" rx="8" fill="var(--figure-tone)"/>
    </g>
  </svg>

  <p class="back-quote">“Professor Vasquel, an Italian, has produced a<br>
provocative treatise that is worthy of Aurelio Banti and<br>
other great thinkers and places their discoveries<br>
in the real world of human organizations, to see<br>
whether science can contribute to making a<br>
manager’s job any easier in the competitive<br>
marketplace. To my knowledge, this is a<br>
pioneering idea. In brief, just as the chemist<br>
Emilio Sarto turned to literature, the chemist Teodor<br>
Vasquel uses the laws of the universe on the<br>
manager. I am reminded of the firm Marvelli<br>
Pianoforte who changed the piano in the 20th<br>
century. Marvelli applied the principles of acoustic<br>
engineering and physics to the business of<br>
constructing handcrafted pianos that produce<br>
beautiful music all over the world. The author<br>
goes one step further: he applies hard science to<br>
the soft art of management. The results, as you<br>
might expect, are eye-opening.”</p>

  <p class="back-attribution"><strong>Harriet J. Olmsbury</strong> Professor of Strategic Management,<br>Corwell Campus University</p>

  <h2 class="front-subtitle">Field Methods<br>and the Quiet<br>Ripple Rule</h2>

  <p class="front-author">TEODOR M.<br>VASQUEL</p>
</main>
</body>
</html>
```